Criação de Papelaria (6 itens) para Associações, ONGs ou Comunidades
" TORVI coordena recursos e competências com parceiros que realizam ações nos âmbitos da deficiência física e mental/intelectual, e dos jovens socialmente vulneráveis. TORVI apoia ações para e com as pessoas com deficiência, focando na inclusão social e no empoderamento, em especial maneira na formação profissional. TORVI apoia crianças e adolescentes socialmente vulneráveis (e as relativas famílias) realizando atividades nos setores de saúde, educação e cultura. O nome da organização manda à ideia de colocar-se em ação em relação ao apoio a projetos e programas sociais e de saúde no sentido amplo do termo. TORVI foi escolhido porque manda ao fogo, à ação, algo que faz acontecer, com carinho típico de quem cozinha, assa. "

```html
<!DOCTYPE html>
<html lang="pt-BR">
<head>
<meta charset="UTF-8">
<title>TORVI — Envelopes</title>
<link href="https://fonts.googleapis.com/css2?family=Montserrat:wght@800&family=Tinos&display=swap" rel="stylesheet">
<style>
  :root {
    --brand-red: #a3252c;
    --stripe-grey: #4a4a4a;
    --stripe-light: #b9b9b9;
    --paper: #ffffff;
    --paper-shade: #ececec;
    --backdrop: #e4e2df;
    --text-grey: #3c3c3c;
  }
  * { margin: 0; padding: 0; box-sizing: border-box; }
  html, body { width: 1200px; height: 1200px; overflow: hidden; }
  body { background: var(--backdrop); position: relative; }

  .envelope {
    position: absolute;
    left: 137px;
    width: 926px;
    background: linear-gradient(160deg, var(--paper) 40%, var(--paper-shade) 100%);
    box-shadow: 0 6px 18px rgba(0,0,0,0.18);
    overflow: hidden;
  }
  .envelope--back { top: 60px; height: 528px; }
  .envelope--front { top: 679px; height: 389px; }

  .envelope__flap { position: absolute; left: 0; top: 0; width: 926px; height: 300px; }

  .brand-name {
    position: absolute;
    font-family: "Montserrat", sans-serif;
    font-weight: 800;
    color: var(--brand-red);
    letter-spacing: 1px;
    line-height: 1;
  }
  .envelope--back .brand-name { left: 48px; top: 408px; font-size: 36px; }

  .brand-lockup { position: absolute; left: 70px; top: 46px; display: flex; align-items: center; gap: 14px; }
  .brand-lockup__dot { width: 72px; height: 72px; border-radius: 50%; background: var(--brand-red); }
  .brand-lockup .brand-name { position: static; font-size: 60px; }

  .contact-list {
    position: absolute;
    right: 66px;
    top: 342px;
    list-style: none;
    font-family: "Tinos", serif;
    font-size: 14px;
    color: var(--text-grey);
  }
  .contact-list li {
    display: flex;
    justify-content: flex-end;
    align-items: center;
    gap: 12px;
    height: 29px;
  }
  .contact-list li.gap-before { margin-top: 8px; }
  .contact-list svg { width: 16px; height: 16px; fill: var(--brand-red); flex: none; }

  .stripe { position: absolute; left: 0; width: 100%; }
  .envelope--back .stripe--main { top: 508px; height: 9px; background: var(--stripe-grey); }
  .envelope--back .stripe--thin { top: 521px; height: 2px; background: var(--stripe-light); }
  .envelope--front .stripe--main { top: 356px; height: 6px; background: var(--brand-red); }
  .envelope--front .stripe--thin { top: 367px; height: 4px; background: var(--stripe-light); }
</style>
</head>
<body>

<section class="envelope envelope--back">
  <svg class="envelope__flap" viewBox="0 0 926 300" aria-hidden="true">
    <path d="M0 0 L926 0 L926 20 Q926 34 908 44 L490 276 Q463 290 436 276 L18 44 Q0 34 0 20 Z"
          fill="#f7f7f7" stroke="#d6d6d6" stroke-width="2"/>
    <path d="M12 44 L436 282 Q463 296 490 282 L914 44" fill="none" stroke="rgba(0,0,0,0.06)" stroke-width="6"/>
  </svg>

  <span class="brand-name">TORVI</span>

  <ul class="contact-list">
    <li>Endereço completo - Cidade - Estado
      <svg viewBox="0 0 16 16"><path d="M8 0a5.5 5.5 0 0 0-5.5 5.5C2.5 10 8 16 8 16s5.5-6 5.5-10.5A5.5 5.5 0 0 0 8 0zm0 8a2.5 2.5 0 1 1 0-5 2.5 2.5 0 0 1 0 5z"/></svg>
    </li>
    <li>(00) 0000-0000 | (00) 000000-0000
      <svg viewBox="0 0 16 16"><path d="M2 5c0-2 2-3 6-3s6 1 6 3v1h-3V4.5H5V6H2zm1 2h10l1 7H2zm5 1.5a2 2 0 1 0 0 4 2 2 0 0 0 0-4z"/></svg>
    </li>
    <li>(00) 0000-0000 | (00) 000000-0000
      <svg viewBox="0 0 16 16"><path d="M4.5 0h7A1.5 1.5 0 0 1 13 1.5v13a1.5 1.5 0 0 1-1.5 1.5h-7A1.5 1.5 0 0 1 3 14.5v-13A1.5 1.5 0 0 1 4.5 0zM5 2v10h6V2zm3 11a1 1 0 1 0 0 2 1 1 0 0 0 0-2z"/></svg>
    </li>
    <li class="gap-before">seuemail@seuemail.com.br
      <svg viewBox="0 0 16 16"><path d="M0 3h16v10H0zm1.5 1.5v.3L8 9l6.5-4.2v-.3zm0 2.1v5h13v-5L8 10.8z"/></svg>
    </li>
    <li>www.torviassociacao.org.br
      <svg viewBox="0 0 16 16"><path d="M8 0a8 8 0 1 0 0 16A8 8 0 0 0 8 0zm5.9 7h-2.4a12 12 0 0 0-1-4.6A6 6 0 0 1 13.9 7zM8 2c.8 1 1.4 2.8 1.5 5h-3C6.6 4.8 7.2 3 8 2zM5.5 2.4A12 12 0 0 0 4.5 7H2.1a6 6 0 0 1 3.4-4.6zM2.1 9h2.4a12 12 0 0 0 1 4.6A6 6 0 0 1 2.1 9zM8 14c-.8-1-1.4-2.8-1.5-5h3c-.1 2.2-.7 4-1.5 5zm2.5-.4a12 12 0 0 0 1-4.6h2.4a6 6 0 0 1-3.4 4.6z"/></svg>
    </li>
  </ul>

  <div class="stripe stripe--main"></div>
  <div class="stripe stripe--thin"></div>
</section>

<section class="envelope envelope--front">
  <div class="brand-lockup">
    <span class="brand-lockup__dot"></span>
    <span class="brand-name">TORVI</span>
  </div>
  <div class="stripe stripe--main"></div>
  <div class="stripe stripe--thin"></div>
</section>

</body>
</html>
```